Flyer-Design für Initiativbewerbung
Zielgruppe
Wir sind ein Buchhaltungsbüro. Mit diesem Flyer möchten wir uns bei Steuerberater als freier Mitarbeiter bewerben als initiativ Bewerbung! Ich lade Bilder von mir selbst mit hoch um so noch persönlicher zu werden. Die Bilder können gerne bearbeitet werden und Ausschnitte gezogen werden. Es soll sehr persönlich rüber kommen
Aufgabenstellung
Flyer sollte Din A Lang sein als Endformat, also gerne auch mehrseitig und max. 20 g haben
Sie können auch Textpassagen duplizieren und auf eine Vorderseite etc machen.
Es soll persönlich wirken obwohl es ein Werbeversand. Anbei auch das Logo unserer Firma.
Ich bin auch offen das Logo in Schwarz weiß darzustellen um so vom Blau wegzukommen.
Ich lasse mich gerne überraschen.
Text
Initiativ Bewerbung freier Mitarbeiter für Ihre Kanzlei
Sehr geehrte Damen und Herren,
gerne bewerben wir uns als freier Mitarbeiter im Rahmen des

```html
<!DOCTYPE html>
<html lang="de">
<head>
<meta charset="utf-8">
<title>Initiativ Bewerbung – Flyer DIN lang</title>
<link rel="stylesheet" href="https://fonts.googleapis.com/css2?family=Barlow:wght@400;500;600&display=swap">
<style>
  :root {
    --page-bg: #ffffff;
    --panel-light: #b8c3e8;
    --brand-blue: #0f5aae;
    --brand-blue-deep: #0b4f9f;
    --ink: #1d2a57;
    --list-blue: #5d87cf;
    --rule-blue: #2f6bc4;
    --white: #ffffff;
    --photo-top: #dfe6f4;
    --photo-bottom: #9fb2cf;
  }
  * { margin: 0; padding: 0; box-sizing: border-box; }
  html, body {
    width: 1200px; height: 473px; overflow: hidden;
    background: var(--page-bg);
    font-family: "Barlow", Arial, sans-serif;
    color: var(--ink);
  }
  .spread { position: relative; width: 1200px; height: 473px; }
  .panel {
    position: absolute; top: 24px; width: 200px; height: 424px;
    box-shadow: 2px 3px 5px rgba(0,0,0,0.28);
    overflow: hidden;
  }
  .panel--front { left: 389px; background: var(--panel-light); }
  .panel--letter { left: 611px; background: var(--panel-light); }

  /* Front panel */
  .portrait {
    position: absolute; left: 0; top: 0; width: 200px; height: 266px;
    background: linear-gradient(160deg, var(--photo-top) 0%, #c9d3e6 50%, var(--photo-bottom) 100%);
  }
  .title-band {
    position: absolute; left: 0; top: 266px; width: 200px; height: 41px;
    text-align: center; background: var(--panel-light);
  }
  .title-band__head {
    margin-top: 9px; font-size: 10.5px; font-weight: 500;
    letter-spacing: 2.6px; color: var(--white);
  }
  .title-band__sub {
    margin-top: 3px; font-size: 6.8px; font-weight: 500;
    letter-spacing: 0.7px; color: var(--ink);
  }
  .brand-block {
    position: absolute; left: 0; top: 307px; width: 200px; height: 117px;
    background: var(--brand-blue); text-align: center; color: var(--white);
  }
  .brand-mark {
    display: block; width: 16px; height: 16px; margin: 26px auto 8px;
    background: var(--white);
  }
  .brand-name { font-size: 15px; font-weight: 400; letter-spacing: 0.6px; line-height: 1; }
  .brand-suffix { margin-top: 4px; font-size: 6px; letter-spacing: 3px; }

  /* Letter panel */
  .letter { position: absolute; left: 20px; top: 0; width: 165px; font-size: 6.6px; line-height: 13px; }
  .letter p { position: absolute; left: 0; width: 165px; }
  .services {
    position: absolute; left: 0; top: 117px; width: 178px; height: 57px;
    background: var(--white); list-style: none; padding: 3px 0 0 10px;
  }
  .services li {
    color: var(--list-blue); font-size: 6.2px; letter-spacing: 0.5px; line-height: 12.8px;
  }
  .services li::before { content: "•"; margin-right: 8px; }
  .signature-rule {
    position: absolute; left: 0; top: 268px; width: 178px; height: 1px; background: var(--rule-blue);
  }
  .signature-name { top: 272px; font-size: 6px; letter-spacing: 0.3px; }

  .contact {
    position: absolute; left: 0; top: 303px; width: 200px; height: 121px;
    background: var(--brand-blue-deep); color: var(--white); text-align: center;
  }
  .contact__head { margin-top: 16px; font-size: 6.8px; letter-spacing: 2px; font-weight: 500; }
  .contact__rule { width: 160px; height: 1px; margin: 6px auto 8px; background: rgba(255,255,255,0.7); }
  .contact__line { font-size: 6.6px; line-height: 12.8px; font-weight: 500; }
  .contact__icon { display: inline-block; vertical-align: -1px; margin-right: 3px; }
</style>
</head>
<body>
<main class="spread">

  <section class="panel panel--front">
    <div class="portrait" role="img" aria-label="Porträtfoto des Inhabers im hellen Sakko vor hellem Hintergrund"></div>
    <div class="title-band">
      <div class="title-band__head">INITIATIV BEWERBUNG</div>
      <div class="title-band__sub">FREIER MITARBEITER FÜR IHRE KANZLEI</div>
    </div>
    <div class="brand-block">
      <span class="brand-mark"></span>
      <div class="brand-name">ZAHLENWERK</div>
      <div class="brand-suffix">GmbH</div>
    </div>
  </section>

  <section class="panel panel--letter">
    <div class="letter">
      <p style="top:17px">Sehr geehrte Damen und Herren,</p>
      <p style="top:43px">gerne bewerben wir uns als freier Mitarbeiter im Rahmen des § 17 BOStB für Ihre Kanzlei.</p>
      <p style="top:81px">Gerne übernehmen wir für Sie im Rahmen der freien Mitarbeiter:</p>
      <ul class="services">
        <li>FINANZBUCHHALTUNG</li>
        <li>LOHNBUCHHALTUNG (AUCH BAULOHN)</li>
        <li>JAHRESABSCHLUSS</li>
        <li>STEUERERKLÄRUNGEN</li>
      </ul>
      <p style="top:184px">Fachliche Erfahrungen bestehen seit über 20 Jahren. Die Tätigkeit auf diversen branchenübli­chen Abrechnungsprogrammen ist uns vertraut.</p>
      <p style="top:235px">Mit freundlichen Grüßen</p>
      <div class="signature-rule"></div>
      <p class="signature-name">TOBIAS KELLNER</p>
    </div>
    <div class="contact">
      <div class="contact__head">KONTAKTDATEN:</div>
      <div class="contact__rule"></div>
      <div class="contact__line">Zahlenwerk GmbH</div>
      <div class="contact__line">Lindenfeldweg 12</div>
      <div class="contact__line">70123 Musterstadt</div>
      <div class="contact__line">
        <svg class="contact__icon" width="5" height="7" viewBox="0 0 5 7" aria-hidden="true"><path d="M1 0.5 C3.5 1.5 3.5 5.5 1 6.5" fill="none" stroke="#fff" stroke-width="1.2"/></svg>0711/12345678
      </div>
      <div class="contact__line">
        <svg class="contact__icon" width="8" height="6" viewBox="0 0 8 6" aria-hidden="true"><rect x="0.4" y="0.4" width="7.2" height="5.2" fill="none" stroke="#fff" stroke-width="0.7"/><path d="M0.4 0.6 L4 3.4 L7.6 0.6" fill="none" stroke="#fff" stroke-width="0.7"/></svg>info@zahlenwerk-beispiel.de
      </div>
    </div>
  </section>

</main>
</body>
</html>
```